Brisk Hive 360 Postcard Design, Double-Sided

Please read carefully and see attached. Designers that do not follow these instructions will not be selected. Limit ONE design submission per artist. The ONE design submission shall show both the front and the back designs. Designs must comply with the attached dismensions accounting for the bleed area to prevent designs from being cut off during printing. The attached business card and door tag designs have already been created, printed and are in use. The postcard shall be similar in design to the attached business card and door tag. All of the information that you need is attached. The overall size is 4.12" x 6.12" for the front. The back is different, see attached and scale to match template. I would like the Veteran Owned Business logo added as well. It would also be nice to see my photo incorporated somehow. I like the yellow on the door tag. It helps build contrast and pops out. Again, one design submission per designer that shows both the front and the back.

Target Market(s)

Please read all instructions and see attached.

Industry/Entity Type

Requirements
Must have
• Please read all instructions and see attached.
Nice to have
Should not have

```html
<!DOCTYPE html>
<html lang="en">
<head>
<meta charset="utf-8">
<title>Brisk Hive 360 Postcard – Front and Back</title>
<link rel="stylesheet" href="https://fonts.googleapis.com/css2?family=Montserrat:ital,wght@1,900&family=Roboto+Condensed:wght@400;700&family=Roboto:wght@400&display=swap">
<style>
  :root {
    --page: #e4e4e4;
    --ink: #050505;
    --paper: #ffffff;
    --silver-light: #f4f4f4;
    --silver-mid: #c9c9c9;
    --silver-dark: #9d9d9d;
    --accent-yellow: #f2e600;
    --photo-blue: #3c5a86;
    --photo-gray: #b9bcc2;
    --wood-light: #d9ab6f;
    --wood-dark: #9a6a38;
    --shirt-gray: #c8c8c8;
  }
  * { box-sizing: border-box; margin: 0; padding: 0; }
  html, body { width: 1200px; height: 800px; overflow: hidden; background: var(--page); }
  .canvas { position: relative; width: 1200px; height: 800px; }

  .card {
    position: absolute; top: 212px; width: 560px; height: 377px;
    background: var(--ink); overflow: hidden;
    box-shadow: 0 6px 18px rgba(0,0,0,.25);
  }
  .card-front { left: 20px; }
  .card-back { left: 620px; }

  .block { position: absolute; }
  .silver { background: linear-gradient(100deg, var(--silver-light) 0%, var(--silver-mid) 45%, var(--paper) 70%, var(--silver-dark) 100%); }

  /* FRONT */
  .front-photo {
    left: 0; top: 22px; width: 258px; height: 150px;
    background: linear-gradient(110deg, var(--photo-gray) 0%, #7d8796 45%, var(--photo-blue) 70%, #1e2f4d 100%);
    clip-path: polygon(0 0, 92% 0, 100% 100%, 0 100%);
  }
  .front-services {
    left: 232px; top: 22px; width: 328px; height: 136px;
    border-top: 2px solid var(--silver-dark);
    padding: 14px 14px 0 0; text-align: right; color: var(--paper);
    font-family: "Roboto Condensed", sans-serif;
  }
  .services-title {
    display: inline-block; font-family: "Montserrat", sans-serif; font-weight: 900; font-style: italic;
    font-size: 15px; border-bottom: 2px solid var(--paper); padding-bottom: 2px; margin-bottom: 8px;
  }
  .services-list { font-size: 13.5px; line-height: 21px; }

  .front-brand {
    left: 0; top: 172px; width: 300px; height: 135px; background: var(--paper);
    clip-path: polygon(0 0, 86% 0, 100% 100%, 0 100%);
    display: flex; align-items: center; justify-content: center; gap: 8px; padding-right: 40px;
  }
  .brand-dot { width: 14px; height: 14px; border-radius: 50%; background: var(--ink); }
  .brand-name { font-family: "Roboto Condensed", sans-serif; font-weight: 700; font-size: 24px; color: var(--ink); }

  .front-profile {
    left: 272px; top: 158px; width: 288px; height: 140px;
    clip-path: polygon(0 0, 100% 0, 100% 100%, 13% 100%);
    text-align: right; padding: 10px 14px 0 0; font-family: "Roboto Condensed", sans-serif; color: var(--ink);
  }
  .profile-name {
    display: inline-block; font-family: "Montserrat", sans-serif; font-weight: 900; font-style: italic;
    font-size: 19px; border-bottom: 2px solid var(--ink); padding-bottom: 1px;
  }
  .profile-role { font-family: "Montserrat", sans-serif; font-weight: 900; font-style: italic; font-size: 13px; margin: 4px 0 6px; }
  .profile-points { font-size: 12.5px; line-height: 19px; }

  .front-contact {
    left: 0; top: 330px; width: 560px; height: 47px;
    display: flex; align-items: center; justify-content: space-between; padding: 0 16px 0 70px;
    font-family: "Roboto", sans-serif; font-size: 13px; color: var(--ink);
  }
  .contact-col { line-height: 19px; }
  .contact-col.right-align { text-align: right; }
  .contact-line { display: flex; align-items: center; gap: 5px; }
  .right-align .contact-line { justify-content: flex-end; }
  .icon { width: 11px; height: 11px; fill: var(--ink); flex: none; }
  .contact-cta {
    font-family: "Montserrat", sans-serif; font-weight: 900; font-style: italic; font-size: 12px;
    border-bottom: 2px solid var(--ink); padding-bottom: 1px;
  }

  /* BACK */
  .back-strip {
    left: 0; top: 34px; width: 470px; height: 46px; border: 2px solid var(--accent-yellow);
    display: flex; justify-content: space-between; align-items: center; padding: 0 30px 0 20px;
    font-family: "Roboto", sans-serif; font-size: 12.5px; color: var(--ink);
  }
  .back-strip .contact-line { line-height: 18px; }
  .stamp-box { left: 484px; top: 20px; width: 60px; height: 62px; background: var(--paper); border: 3px solid var(--ink); }
  .address-area { left: 348px; top: 82px; width: 212px; height: 218px; background: var(--paper); }
  .address-area-top { left: 470px; top: 48px; width: 90px; height: 36px; background: var(--paper); }
  .address-line { position: absolute; left: 22px; right: 14px; height: 1.5px; background: var(--ink); }

  .back-tools {
    left: 0; top: 80px; width: 335px; height: 152px;
    background: linear-gradient(180deg, var(--wood-light) 0%, #c8935a 55%, var(--wood-dark) 100%);
  }
  .back-profile {
    left: 0; top: 218px; width: 335px; height: 82px;
    padding: 12px 0 0 30px; color: var(--ink);
  }
  .back-profile .profile-name { font-size: 15px; }
  .back-profile .profile-role { font-size: 10px; margin-top: 3px; }
  .back-portrait {
    left: 250px; top: 196px; width: 78px; height: 104px;
    background: linear-gradient(180deg, #b58d70 0%, var(--shirt-gray) 45%, #a9a9a9 100%);
    border-radius: 28px 28px 0 0;
  }
</style>
</head>
<body>
<main class="canvas">

  <section class="card card-front" aria-label="Postcard front">
    <div class="block front-photo" role="img" aria-label="Photo of a technician in a blue uniform working on an electrical panel"></div>

    <div class="block front-services">
      <div class="services-title">SERVICES:</div>
      <div class="services-list">
        Assembly • Small Repairs • Wifi Router Setup •<br>
        Wireless Device Setup • Odd Jobs •<br>
        Fabrication • Hanging Items
      </div>
    </div>

    <div class="block front-brand">
      <span class="brand-dot"></span>
      <span class="brand-name">Brisk Hive 360</span>
    </div>

    <div class="block front-profile silver">
      <div class="profile-name">DANA R. HOLLOWAY</div>
      <div class="profile-role">OWNER &amp; HANDYMAN</div>
      <div class="profile-points">
        Fast Response • High Quality •<br>
        Veteran Owned •<br>
        Fair Pricing
      </div>
    </div>

    <div class="block front-contact silver">
      <div class="contact-col right-align">
        <div class="contact-line">(555) 014-2290
          <svg class="icon" viewBox="0 0 24 24"><path d="M6.6 10.8a15 15 0 0 0 6.6 6.6l2.2-2.2c.3-.3.7-.4 1-.2 1.1.4 2.3.6 3.6.6.6 0 1 .4 1 1V20c0 .6-.4 1-1 1A17 17 0 0 1 3 4c0-.6.4-1 1-1h3.5c.6 0 1 .4 1 1 0 1.3.2 2.5.6 3.6.1.3 0 .7-.2 1z"/></svg>
        </div>
        <div class="contact-line">Lakemont, Florida
          <svg class="icon" viewBox="0 0 24 24"><path d="M12 2a7 7 0 0 0-7 7c0 5 7 13 7 13s7-8 7-13a7 7 0 0 0-7-7zm0 9.5A2.5 2.5 0 1 1 12 6.5a2.5 2.5 0 0 1 0 5z"/></svg>
        </div>
      </div>
      <div class="contact-col right-align">
        <div class="contact-line">Service@BriskHive360.com
          <svg class="icon" viewBox="0 0 24 24"><path d="M2 5h20v14H2zm2 2v.5l8 5 8-5V7l-8 5z"/></svg>
        </div>
        <div class="contact-line">BriskHive360.com
          <svg class="icon" viewBox="0 0 24 24"><circle cx="12" cy="12" r="9" fill="none" stroke="#050505" stroke-width="2"/><path d="M3 12h18M12 3c3 3 3 15 0 18M12 3c-3 3-3 15 0 18" fill="none" stroke="#050505" stroke-width="1.5"/></svg>
        </div>
      </div>
      <div class="contact-cta">CONTACT US</div>
    </div>
  </section>

  <section class="card card-back" aria-label="Postcard back">
    <div class="block address-area-top"></div>
    <div class="block address-area">
      <span class="address-line" style="top:52px"></span>
      <span class="address-line" style="top:88px"></span>
      <span class="address-line" style="top:124px"></span>
      <span class="address-line" style="top:160px"></span>
      <span class="address-line" style="top:196px"></span>
    </div>
    <div class="block stamp-box"></div>

    <div class="block back-strip silver">
      <div class="contact-col">
        <div class="contact-line">
          <svg class="icon" viewBox="0 0 24 24"><path d="M6.6 10.8a15 15 0 0 0 6.6 6.6l2.2-2.2c.3-.3.7-.4 1-.2 1.1.4 2.3.6 3.6.6.6 0 1 .4 1 1V20c0 .6-.4 1-1 1A17 17 0 0 1 3 4c0-.6.4-1 1-1h3.5c.6 0 1 .4 1 1 0 1.3.2 2.5.6 3.6.1.3 0 .7-.2 1z"/></svg>
          (555) 014-2290</div>
        <div class="contact-line">
          <svg class="icon" viewBox="0 0 24 24"><path d="M12 2a7 7 0 0 0-7 7c0 5 7 13 7 13s7-8 7-13a7 7 0 0 0-7-7zm0 9.5A2.5 2.5 0 1 1 12 6.5a2.5 2.5 0 0 1 0 5z"/></svg>
          Lakemont, Florida</div>
      </div>
      <div class="contact-col">
        <div class="contact-line">
          <svg class="icon" viewBox="0 0 24 24"><path d="M2 5h20v14H2zm2 2v.5l8 5 8-5V7l-8 5z"/></svg>
          Service@BriskHive360.com</div>
        <div class="contact-line">
          <svg class="icon" viewBox="0 0 24 24"><circle cx="12" cy="12" r="9" fill="none" stroke="#050505" stroke-width="2"/><path d="M3 12h18M12 3c3 3 3 15 0 18M12 3c-3 3-3 15 0 18" fill="none" stroke="#050505" stroke-width="1.5"/></svg>
          BriskHive360.com</div>
      </div>
    </div>

    <div class="block back-tools" role="img" aria-label="Photo of hand tools laid out on a wooden plank surface"></div>
    <div class="block back-profile silver">
      <div class="profile-name">DANA R. HOLLOWAY</div>
      <div class="profile-role">OWNER &amp; HANDYMAN</div>
    </div>
    <div class="block back-portrait" role="img" aria-label="Portrait photo of the business owner in a gray shirt"></div>
  </section>

</main>
</body>
</html>
```